Website design for Maple Nook Kidcare

I need a website designed for my daycare business, Maple Nook Kidcare, now that I have a new logo. My former website was ok but simple and I did not have a logo yet. It also was created by me using a template and was entirely pink. I loved the bright, happy feel of it but worried it might not appeal as much to potential clients who have sons. Therefore, I need a site which will appeal to both genders while still keeping the cheerful color scheme of my new logo, which has pinks, blue, green and cream.

Reason: Hello! I am still trying to download my new logo and am sorry it is taking me so long. Hopefully I will it posted by the end of today (US Eastern Standard Time). Thank you all very much for your patience!

Hello! I have finally managed to upload my new logo for you to use in designing my website. I'm sorry it took so long and greatly appreciate your time and creative efforts! I look forward to seeing what is submitted based on my logo design and its style/colors.

Many thanks!

Reason: As I've been traveling and posted my logo file late, I am extending my deadline. I am now back and can focus on providing more and better feedback. I appreciate your patience and submissions very much!

Reason: I need more time to provide feedback and make decisions.

Industry/Entity Type

Daycare

Colors
0192cd
33a6d7
86cae7
cadf82
fbf289
add136
e34197

```html
<!DOCTYPE html>
<html lang="en">
<head>
<meta charset="utf-8">
<title>Maple Nook Kidcare</title>
<link href="https://fonts.googleapis.com/css2?family=Open+Sans:wght@400;600;700&family=Quicksand:wght@500;700&family=Sniglet:wght@400;800&display=swap" rel="stylesheet">
<style>
:root{
  --pink:#e34197;
  --blue:#0192cd;
  --blue-mid:#33a6d7;
  --blue-light:#86cae7;
  --green:#add136;
  --green-deep:#8fb82a;
  --lime:#cadf82;
  --cream:#fdf7dc;
  --yellow:#fbf289;
  --brown:#6b3f1f;
  --text:#444;
  --white:#fff;
}
*{box-sizing:border-box;margin:0;padding:0}
html,body{width:1200px;height:2747px;overflow:hidden;background:var(--white)}
body{position:relative;font-family:"Open Sans",sans-serif;color:var(--text)}
.abs{position:absolute}
.display{font-family:"Sniglet",sans-serif;font-weight:800}

/* header & hero */
.hero-photo{left:0;top:0;width:1200px;height:700px;background:linear-gradient(180deg,#5fa6dc 0%,#8cc4e8 38%,#6fb2c8 46%,#d9c4a2 56%,#c7ab84 100%)}
.topbar{left:0;top:0;width:1200px;height:56px;background:var(--blue)}
.topbar-accent{left:0;top:56px;width:1200px;height:5px;background:var(--green)}
.nav{right:54px;top:0;height:56px;display:flex;align-items:center;gap:28px;list-style:none}
.nav li{color:var(--white);font-weight:700;font-size:15px;letter-spacing:.2px}
.brand-badge{left:38px;top:0;width:246px;height:236px;border-radius:50%;background:var(--cream);border:6px solid var(--white);box-shadow:0 3px 8px rgba(0,0,0,.25);display:flex;align-items:center;justify-content:center;text-align:center}
.brand-name{font-family:"Sniglet",sans-serif;font-weight:800;color:var(--pink);font-size:34px;line-height:1.1}
.hero-box{left:150px;top:352px;height:154px;background:rgba(253,247,220,.85);border-radius:8px;padding:20px 26px}
.hero-title{font-size:50px;line-height:56px;color:var(--pink)}
.hero-title .accent{color:var(--blue)}

/* intro */
.intro{left:0;top:700px;width:1200px;text-align:center}
.intro h1{font-family:"Quicksand",sans-serif;font-weight:700;color:var(--blue);font-size:46px;margin-top:20px;line-height:54px}
.intro .tagline{font-family:"Sniglet",sans-serif;font-size:17px;color:var(--pink);margin-top:4px}
.intro p{font-size:13.5px;line-height:19px;width:1080px;margin:4px auto 0}

/* licence band */
.licence-photo{left:0;top:906px;width:1200px;height:410px;background:radial-gradient(ellipse at 30% 50%,#6e7a55 0%,#3c4a2c 55%,#1f2a1a 100%)}
.licence-text{left:0;top:1036px;width:1200px;text-align:center;color:var(--white);font-size:34px;line-height:46px}
.btn-explore{left:516px;top:1147px;width:168px;height:44px;background:var(--green);color:var(--white);font-weight:700;font-size:16px;display:flex;align-items:center;justify-content:center}

/* feature cards */
.feature{top:1342px;width:346px}
.feature-photo{width:346px;height:242px;border-bottom:6px solid var(--green)}
.feature h3{font-size:28px;margin-top:14px;line-height:32px}
.feature p{font-size:14px;line-height:19px;color:#333;width:310px}
.f-blue{color:var(--blue)}
.f-pink{color:var(--pink)}
.f-green{color:var(--green-deep)}

/* services */
.services{left:0;top:1738px;width:1200px;height:334px;background:linear-gradient(180deg,var(--blue-mid) 0%,var(--blue) 100%)}
.section-label{color:var(--white);font-size:29px;letter-spacing:.5px}
.services-list{left:52px;top:80px;list-style:none;color:var(--white);font-size:13.5px;line-height:21.4px}
.services-list li::first-letter{color:var(--yellow)}
.video-frame{left:784px;top:80px;width:356px;height:218px;background:var(--cream);padding:7px}
.video-still{width:100%;height:100%;background:linear-gradient(135deg,#c9a27a 0%,#e8c9b3 45%,#b57d63 100%)}

/* news */
.news{left:51px;top:2092px;width:1100px}
.news h2{color:var(--pink);font-size:29px}
.news p{font-size:14px;line-height:19px;color:#333;margin-top:4px}
.btn-more{margin-top:12px;width:129px;height:30px;background:var(--blue);color:var(--white);font-weight:700;font-size:12px;border-radius:3px;display:flex;align-items:center;justify-content:center}

/* testimonials */
.testimonials{left:0;top:2244px;width:1200px;height:328px;background:var(--cream);text-align:center}
.testimonials h2{font-family:"Quicksand",sans-serif;color:var(--blue);font-weight:700;font-size:40px;margin-top:20px;line-height:52px}
.testimonials .sub{font-family:"Sniglet",sans-serif;font-size:16px;color:#333}
.quote-card{top:128px;width:265px;height:170px;background:var(--white);border:1px solid #e4dcb8;border-radius:8px;text-align:left;padding:18px 18px 0}
.quote-card blockquote{font-size:14px;line-height:19px;color:#555;padding-left:8px}
.quote-rule{position:absolute;left:12px;right:12px;top:102px;height:3px;background:var(--green)}
.client{position:absolute;left:18px;top:116px;display:flex;align-items:center;gap:16px;font-size:13px;font-weight:600;color:#333}
.client-photo{width:40px;height:40px;background:linear-gradient(135deg,#d9b38a,#8a6a4c)}

/* footer */
.footer-band{left:0;top:2572px;width:1200px;height:6px;background:var(--pink)}
.footer-touch{left:30px;top:2606px;display:flex;align-items:center;gap:8px;font-size:13px;font-weight:600;color:#222}
.social{width:26px;height:26px;border-radius:3px}
.footer-nav{left:24px;top:2654px;display:flex;gap:18px;list-style:none;font-size:11px;font-weight:700;color:#222}
.copyright{left:24px;top:2677px;font-size:11px;color:#666}
.footer-brand{left:928px;top:2604px;width:220px;height:130px;display:flex;align-items:center;justify-content:center;text-align:center}
</style>
</head>
<body>

<div class="abs hero-photo" role="img" aria-label="Children running barefoot along a sunny beach by the sea"></div>
<div class="abs topbar"></div>
<div class="abs topbar-accent"></div>
<ul class="abs nav">
  <li>HOME</li><li>ABOUT US</li><li>SERVICES</li><li>HOURSE AND FEES</li><li>POLICIES</li><li>CONTACT US</li><li>PHOTOS</li><li>TESTIMONIALS</li>
</ul>
<div class="abs brand-badge"><span class="brand-name">Maple Nook<br>Kidcare</span></div>
<div class="abs hero-box">
  <div class="hero-title display">Are your kids ready<br>for <span class="accent">Maple Nook?</span></div>
</div>

<section class="abs intro">
  <h1>Maple Nook Kidcare</h1>
  <div class="tagline">Welcome to Maple Nook Kidcare, a playspace where children can play, create, and imagine!</div>
  <p>Welcome to Maple Nook Kidcare, a licensed Group Family Day Care, located in Riverbend's beautiful Hillcrest district. We are located on a pretty, tree-lined block on Linden Lane, between Oak and Elm Avenues. We are a few blocks from the Green Line tram and the Harbor Road bus route, and we offer flexible hourly childcare, making it as easy as possible for busy parents on the go to arrange their children's care.<br>We invite you to learn more about us and hope you will visit us soon!</p>
</section>

<div class="abs licence-photo" role="img" aria-label="Caregiver playing with children in a water sprinkler outdoors"></div>
<div class="abs licence-text">Maple Nook Kidcare is fully licensed by Harbor State<br>Office of Child Care Services</div>
<div class="abs btn-explore">EXPLORE</div>

<article class="abs feature" style="left:41px">
  <div class="feature-photo" role="img" aria-label="Boy doing schoolwork at a desk with coloured pencils" style="background:linear-gradient(135deg,#e9eef2 0%,#9cc7e6 55%,#2f8fd0 100%)"></div>
  <h3 class="display f-blue">Learning</h3>
  <p>We develop age-appropriate activities that introduce and strengthen academic and social skills.</p>
</article>
<article class="abs feature" style="left:422px">
  <div class="feature-photo" role="img" aria-label="Young girl painting colourfully on an easel" style="background:linear-gradient(135deg,#f4d36a 0%,#e86f5a 45%,#f1efe8 100%)"></div>
  <h3 class="display f-pink">Creative</h3>
  <p>We offer children a wide range of creative opportunities including art projects, toddler yoga lessons, afternoon tea parties, dress up play, and a large selection of books and games.</p>
</article>
<article class="abs feature" style="left:806px">
  <div class="feature-photo" role="img" aria-label="Two toddlers sharing a toy together" style="background:linear-gradient(135deg,#e9d5b9 0%,#c89a72 50%,#7d6a5a 100%)"></div>
  <h3 class="display f-green">Sharing</h3>
  <p>We strive to include enrichment activities that extend your child's understanding of the world and their role in it. During our tea parties, for instance, we teach.</p>
</article>

<section class="abs services">
  <h2 class="abs section-label display" style="left:52px;top:26px">SERVICES</h2>
  <ul class="abs services-list">
    <li>&gt; Flexible hourly full and part-time childcare</li>
    <li>&gt; Discount for siblings</li>
    <li>&gt; Small adult: child ratio</li>
    <li>&gt; Daily schedules that vary per the age of children in our care</li>
    <li>&gt; Large selection of books, toys, and games</li>
    <li>&gt; Large, sunny, private backyard with playground equipment such as a toddler slide and sand/water table</li>
    <li>&gt; Art center with easels and a large assortment of arts and crafts supplies</li>
    <li>&gt; Original, creative activities and lessons in subjects such as American Sign Language and Toddler Yoga</li>
    <li>&gt; Afternoon dress-up and tea parties with lessons in good manners</li>
    <li>&gt; Fun-filled field trips to our area's best museums, child activity centers, performances and the Zoo!</li>
    <li>&gt; Assistance with potty-training to help prepare children for pre-school</li>
  </ul>
  <h2 class="abs section-label display" style="left:784px;top:26px">WATCH VIEDO</h2>
  <div class="abs video-frame">
    <div class="video-still" role="img" aria-label="Video still of a caregiver playing with toddlers in a playroom"></div>
    <svg class="abs" style="left:151px;top:82px" width="54" height="54" viewBox="0 0 54 54" aria-hidden="true">
      <circle cx="27" cy="27" r="26" fill="#e34197" stroke="#fff" stroke-width="2"/>
      <path d="M21 16 L39 27 L21 38 Z" fill="#fff"/>
    </svg>
  </div>
</section>

<section class="abs news">
  <h2 class="display">Latest News</h2>
  <p>We are thrilled to have found a new cheerful space with a private backyard! It's large, sunny, and filled with outdoor play equipment such as a toddler slide, sand/water activity table, and lots of toys! Please stay tuned for updates on our program and services as we say goodbye to Winter and hello to Spring!</p>
  <div class="btn-more">READ MORE</div>
</section>

<section class="abs testimonials">
  <h2>Client Testimonial</h2>
  <div class="sub">Read testimonials from Telecommunication clients on their experience with Maple Nook Kidcare Services.</div>
  <div class="abs quote-card" style="left:187px">
    <blockquote>"Lorem ipsum dolor sit amet, consectetur adipiscing elit. Phasellus quis lectus metus, at posuere neque."</blockquote>
    <div class="quote-rule"></div>
    <div class="client"><div class="client-photo" role="img" aria-label="Client portrait"></div>Client Name</div>
  </div>
  <div class="abs quote-card" style="left:467px">
    <blockquote>"Lorem ipsum dolor sit amet, consectetur adipiscing elit. Phasellus quis lectus metus, at posuere neque."</blockquote>
    <div class="quote-rule"></div>
    <div class="client"><div class="client-photo" role="img" aria-label="Client portrait"></div>Client Name</div>
  </div>
  <div class="abs quote-card" style="left:748px">
    <blockquote>"Lorem ipsum dolor sit amet, consectetur adipiscing elit. Phasellus quis lectus metus, at posuere neque."</blockquote>
    <div class="quote-rule"></div>
    <div class="client"><div class="client-photo" role="img" aria-label="Client portrait"></div>Client Name</div>
  </div>
</section>

<div class="abs footer-band"></div>
<div class="abs footer-touch">Stay in touch with us
  <span class="social" style="background:#3b5a9a"></span>
  <span class="social" style="background:#3aa5dc"></span>
  <span class="social" style="background:#c4302b"></span>
  <span class="social" style="background:#1d75b3"></span>
</div>
<ul class="abs footer-nav">
  <li>HOME</li><li>ABOUT US</li><li>SERVICES</li><li>HOURSE AND FEES</li><li>POLICIES</li><li>CONTACT US</li><li>PHOTOS</li><li>TESTIMONIALS</li>
</ul>
<div class="abs copyright">Copyright © 2014 All Rights Reserved</div>
<div class="abs footer-brand"><span class="brand-name">Maple Nook<br>Kidcare</span></div>

</body>
</html>
```